Flyer Design for a Mediation (Rediation on Quiet Rivers)

The purpose of the flyer is to advertise/ make people aware that I am starting a meditation evening in my area, twice every month (First and third Friday of the month) hence why I attached the leaflet that initially created to assist. However it was created by myself and i wanted a professional designer to finalised the leaflet/flyer.

I would like a 2 sided leaflet.
Front of leaflet

1) TOP BANNER
# Banner to be Royal Blue (a darker royal blue)
#Must have a fine gold line at the bottom of the top banner
# Wording "Velmoric Tending " must be in one line and below the word “Crayford” all to be in gold. Please note that wording must be placed to the far left hand side.
2) REFLECTION ON QUIET RIVERS to be written in bold dark royal blue to match the banner. This is to be placed to the centre of the page.
Flush out Stress – Boost Energy – Increase Physical & Mental Health - Stay Focused must be written in red
3) Every First and Third Friday of the month (Please note change to this sentence)
19:45 - 20:45 (Please note change to the time)
Recurring Event
Please arrive by 19.30 for a brief introduction .

4) Our guided Mediation is for over 18’s only. Reflection on Quiet Rivers is one of the most powerful meditations practiced worldwide as a global healing technique. (the wording “Reflection on Quiet Rivers” in this sentence, must be in Gold)

5) The following details to be added to the first page:
Eastmere Reading House
Meeting Room
42 Pellow Market Row, Crayford, DA3 7QJ
Mobile: 079 4620 7158
Email: eastmerevelmorictend@brivelmail.net
Like us on Friendwall: Eastmere Velmic Tending
6) Rediation on Quiet Rivers is one of the most powerful mediation tools for spiritual development. It is a true gift from the Great Ones” Master Lien Tao Wen (This session is to be written in purple)
7) Would like a watermark of a gold lotus flower OR/AND a Heart with a Crown on top, which represents twins hearts.

Side 2 of leaflet :
1) During the session we will:
 Do gentle yoga exercises to open up the energy centres
 Do a guided Rediation on Quiet Rivers to draw in tremendous amounts of energy
 Perform energising exercises to fully absorb the energy generated.

2) We do not charge for the evening but ask for a donation. (This sentence must be in Red)

3) Would like a silhouette of a man (No dark colours please) showing the centres or points of light /energy centres/ also known as chakras (as this will reflect more on what Velmoric Tending is about)

Thank you very much

Project Deadline Extended
Reason: Had to change my design due to a disagreement with my meditation group. Mediation wording and images had to be changed. I have all information. Would like to extend deadline until Sunday07th June 2015 if possible. Thank you and please advise if there are any further charges. Once again my sincere apologises.

Target Market(s)

Everyone interested in spirituality/meditation

Font styles to use
Decorative
Other font styles liked:
• ARIAL

Colors
0455a3
ffc214
6b449b
ffffff

Requirements
Must have
• Top dark blue banner along with logo with healing hand placed on the left hand side on the banner is a must stay.
Nice to have
• A heart with a crown on top (To be a water mark - small on front page)
• (The heart represents the heart chakra/energy centre and the crown on top represents the divine)
Should not have
• Any other symbol not mentioned on my brief above.

```html
<!DOCTYPE html>
<html lang="en">
<head>
<meta charset="utf-8">
<title>Velmoric Tending Crayford – Flyer</title>
<link href="https://fonts.googleapis.com/css2?family=Questrial&family=Arimo:wght@400;700&display=swap" rel="stylesheet">
<style>
  :root{
    --royal:#2b3590;
    --royal-deep:#1f2a7a;
    --gold:#ffc214;
    --gold-soft:#f5c33b;
    --red:#c8161d;
    --orange-red:#e4572e;
    --purple:#5a2a8c;
    --navy-text:#2e3192;
    --link-blue:#1f4f9a;
    --white:#ffffff;
    --lavender:#b7bde3;
    --stage:#e8e6e3;
  }
  *{box-sizing:border-box;margin:0;padding:0}
  html,body{width:1200px;height:1000px;overflow:hidden}
  body{background:var(--stage);position:relative;font-family:"Arimo",Arial,sans-serif}
  .flyer{
    position:absolute;top:142px;width:504px;height:715px;overflow:hidden;
    background:
      linear-gradient(90deg,var(--lavender) 0%,rgba(255,255,255,0) 14%,rgba(255,255,255,0) 86%,var(--lavender) 100%),
      var(--white);
    box-shadow:0 6px 18px rgba(0,0,0,.25);
  }
  .flyer--front{left:91px}
  .flyer--back{left:626px}
  .banner{position:absolute;left:0;top:0;width:100%;height:151px;background:var(--royal)}
  .banner__gold-line{position:absolute;left:0;top:151px;width:100%;height:9px;background:var(--gold)}
  .banner__art{
    position:absolute;left:0;top:0;width:200px;height:151px;
    background:
      radial-gradient(circle at 38% 52%,#fff7c0 0%,#8fe0ff 18%,#2b7fd6 40%,rgba(43,53,144,0) 70%),
      linear-gradient(90deg,#0c1240 0%,var(--royal) 100%);
  }
  .banner__name{
    position:absolute;right:38px;top:60px;color:var(--gold);
    font-family:"Arimo",Arial,sans-serif;font-weight:700;font-size:37px;letter-spacing:.2px;
  }
  .banner__place{
    position:absolute;right:38px;top:105px;color:var(--gold-soft);
    font-family:"Questrial",sans-serif;font-size:25px;
  }
  .front__title{position:absolute;left:0;width:100%;text-align:center;color:var(--navy-text);font-family:"Questrial",sans-serif;line-height:1}
  .front__title--main{top:186px;font-size:62px}
  .front__title--sub{top:238px;font-size:41px}
  .front__benefits{position:absolute;top:282px;left:0;width:100%;text-align:center;color:var(--red);font-weight:700;font-size:17px;line-height:20px}
  .front__schedule{position:absolute;top:342px;left:0;width:100%;text-align:center;color:var(--navy-text);font-family:"Questrial",sans-serif;font-size:15px;line-height:17px}
  .front__glow{
    position:absolute;left:60px;top:395px;width:390px;height:90px;
    background:radial-gradient(ellipse at center,#3b3a9e 0%,rgba(90,80,180,.85) 45%,rgba(140,130,210,0) 75%);
  }
  .front__intro{position:absolute;top:402px;left:0;width:100%;text-align:center;color:var(--white);font-weight:700;font-size:14.5px;line-height:18px}
  .front__intro .accent{color:var(--gold)}
  .front__lotus{
    position:absolute;left:40px;top:440px;width:430px;height:290px;
    background:
      radial-gradient(ellipse at 50% 100%,#fff6d6 0%,#ffd45a 35%,#f2b233 60%,rgba(245,196,80,0) 80%);
    opacity:.85;
  }
  .front__quote{position:absolute;top:497px;left:0;width:100%;text-align:center;color:var(--purple);font-weight:700;font-size:15px;line-height:19px}
  .front__quote .author{font-weight:400;color:var(--purple)}
  .front__venue{position:absolute;top:629px;left:0;width:100%;text-align:center;color:var(--link-blue)}
  .front__venue .where{font-weight:700;font-size:14px;line-height:18px}
  .front__venue .detail{font-size:10.5px;line-height:14px}
  .social-square{display:inline-block;width:11px;height:11px;background:var(--link-blue);vertical-align:-1px;margin-right:3px}
  .back__figure{
    position:absolute;left:112px;top:180px;width:280px;height:315px;
    background:radial-gradient(ellipse at 50% 55%,#dfe3f7 0%,#b9c2ea 45%,rgba(255,255,255,0) 75%);
  }
  .back__heading{position:absolute;top:507px;left:0;width:100%;text-align:center;color:var(--royal-deep);font-weight:700;font-size:19px}
  .back__list{position:absolute;top:544px;left:0;width:100%;text-align:center;color:var(--navy-text);font-family:"Questrial",sans-serif;font-size:13px;line-height:15px}
  .back__list p{margin-bottom:15px}
  .back__list .accent{color:#b09a5e}
  .back__donation{color:var(--orange-red)}
</style>
</head>
<body>

<section class="flyer flyer--front">
  <header class="banner">
    <div class="banner__art" role="img" aria-label="Healing hand radiating light"></div>
    <div class="banner__name">Velmoric Tending</div>
    <div class="banner__place">Crayford</div>
  </header>
  <div class="banner__gold-line"></div>

  <div class="front__lotus" role="img" aria-label="Soft golden lotus flower watermark"></div>

  <h1 class="front__title front__title--main">Reflection</h1>
  <h2 class="front__title front__title--sub">on Quiet Rivers</h2>

  <p class="front__benefits">- Flush Out Stress - Boost Energy - Stay Focused<br>- Increase Physical &amp; Mental Health</p>

  <p class="front__schedule">Every First and Third Friday of the month<br>19:45 - 20:45 Recurring Event<br>Please arrive by 19.30 for a brief introduction</p>

  <div class="front__glow"></div>
  <p class="front__intro">Our guided Mediation is for over 18's only.<br><span class="accent">Reflection on Quiet Rivers</span> is one of<br>the most powerful meditations practiced<br>worldwide as a global healing technique.</p>

  <p class="front__quote">Rediation on Quiet Rivers is<br>one of the most powerful<br>mediation tools for spiritual<br>development. It is a true gift<br>from the Great Ones"<br><span class="author">Master Lien Tao Wen</span></p>

  <div class="front__venue">
    <p class="where">Where? – Eastmere Reading House Meeting Room</p>
    <p class="detail">42 Pellow Market Row, Crayford, DA3 7QJ Mobile: 079 4620 7158</p>
    <p class="detail">mail: eastmerevelmorictend@brivelmail.net</p>
    <p class="detail"><span class="social-square"></span>Like us on Friendwall: Eastmere Velmic Tending</p>
  </div>
</section>

<section class="flyer flyer--back">
  <header class="banner">
    <div class="banner__art" role="img" aria-label="Healing hand radiating light"></div>
    <div class="banner__name">Velmoric Tending</div>
    <div class="banner__place">Crayford</div>
  </header>
  <div class="banner__gold-line"></div>

  <div class="back__figure" role="img" aria-label="Light blue outline of a seated meditating figure with coloured energy centres"></div>

  <h2 class="back__heading">During the session we will:</h2>
  <div class="back__list">
    <p>Do gentle yoga exercises to open up the energy centres.</p>
    <p>Do a guided <span class="accent">Reflection on Quiet Rivers</span><br>to draw in tremendous amounts of energy.</p>
    <p>Perform energising exercises to fully<br>absorb the energy generated.</p>
    <p class="back__donation">We do not charge for the evening but ask for a donation.</p>
  </div>
</section>

</body>
</html>
```